Tap Nest Flow is an under sink water filtration product for the domestic market which will replace the need to purchase bottled water in the home.

The water filter provides safe delicious drinking water at the kitchen sink.

Priced at €2.99 per week

I am looking for a series of five flyers.

Re-develope the attached one and we will get you to develop a series of five more.
Updates

To Designers

This is my first time using this service and therefore is a test with a small investment. None of the designs posted so far are up to the standard required. I do like the parachute idea but would need to be more finished. The original flyer provided with the original brief is without doubt the best by far. 
I am not sure what the next step is however I cannot use anything produced so far.

Target Market(s)

Domestic home owner.

Requirements
Must have
• See attached example
Nice to have
• See attached

```html
<!DOCTYPE html>
<html lang="en">
<head>
<meta charset="utf-8">
<title>Tap Nest Flow – Flyer</title>
<link rel="stylesheet" href="https://fonts.googleapis.com/css2?family=Fredoka:wght@600;700&family=Poppins:wght@700;800&family=Arimo:wght@400;700&display=swap">
<style>
  :root {
    --sky-top: #1b8fd0;
    --sky-mid: #3fb0d8;
    --sky-low: #a6cf45;
    --band-cyan: #12aee3;
    --lime: #c4da3a;
    --royal: #0a55b8;
    --navy: #0d3f9a;
    --teal: #3bb7c9;
    --red: #d9262b;
    --ink: #111111;
    --white: #ffffff;
  }
  * { margin: 0; padding: 0; box-sizing: border-box; }
  html, body { width: 926px; height: 1200px; overflow: hidden; background: var(--white); }
  .flyer {
    position: relative;
    width: 926px;
    height: 1200px;
    overflow: hidden;
    background: var(--lime);
    font-family: "Arimo", Arial, sans-serif;
  }
  .sky {
    position: absolute; left: 0; top: 0; width: 926px; height: 375px;
    background: linear-gradient(180deg, var(--sky-top) 0%, var(--sky-mid) 45%, var(--sky-low) 100%);
  }
  .diagonal-band { position: absolute; left: 0; top: 0; }
  .cyan-band {
    position: absolute; left: 0; top: 375px; width: 926px; height: 137px;
    background: var(--band-cyan);
  }
  .hostess-illustration {
    position: absolute; left: 520px; top: 28px; width: 406px; height: 347px;
    border-radius: 180px 0 0 0;
    background: linear-gradient(160deg, #8a3a2a 0%, #e9a27a 35%, #1f9fe0 70%, #f4f4f4 100%);
    opacity: 0.9;
  }
  .price-badge { position: absolute; left: 18px; top: 8px; width: 210px; height: 200px; }
  .price-badge .badge-text {
    position: absolute; left: 0; top: 0; width: 210px; height: 200px;
    display: flex; flex-direction: column; align-items: center; justify-content: center;
    transform: rotate(-18deg);
    font-family: "Fredoka", sans-serif; color: var(--white); line-height: 0.9;
  }
  .badge-text .only { font-size: 30px; font-weight: 700; margin-left: 40px; }
  .badge-text .amount { font-size: 62px; font-weight: 700; }
  .badge-text .amount small { font-size: 28px; vertical-align: 18px; }
  .badge-text .week { font-size: 42px; font-weight: 700; margin-left: 30px; }

  .headline-question {
    position: absolute; left: 97px; top: 296px; width: 760px;
    font-family: "Fredoka", sans-serif; font-weight: 700; font-size: 96px;
    letter-spacing: 2px; white-space: nowrap;
    -webkit-text-stroke: 6px var(--white); paint-order: stroke fill;
    text-shadow: 3px 4px 0 rgba(0,0,0,0.25);
  }
  .headline-question .dark { color: var(--royal); }
  .headline-question .light { color: var(--teal); }
  .headline-brand {
    position: absolute; left: 0; top: 398px; width: 926px;
    font-family: "Fredoka", sans-serif; font-weight: 700; font-size: 108px;
    color: var(--navy); white-space: nowrap; text-align: center; line-height: 1.1;
  }

  .tagline-main, .tagline-sub {
    position: absolute; left: 0; width: 926px; text-align: center;
    font-family: "Poppins", sans-serif; font-weight: 800; color: var(--red);
    -webkit-text-stroke: 6px var(--white); paint-order: stroke fill;
    white-space: nowrap;
  }
  .tagline-main { top: 538px; font-size: 52px; letter-spacing: -1px; }
  .tagline-sub { top: 600px; font-size: 37px; letter-spacing: 2px; }

  .lead-question {
    position: absolute; left: 39px; top: 654px;
    font-weight: 700; font-size: 25px; color: var(--ink); white-space: nowrap;
  }
  .lead-copy {
    position: absolute; left: 58px; top: 690px; width: 850px;
    font-family: "Poppins", sans-serif; font-weight: 700; font-size: 17px;
    line-height: 30px; color: var(--ink); letter-spacing: -0.4px;
    white-space: nowrap;
  }
  .lead-copy .brand-mention { color: var(--red); }
  .lead-copy .price { color: var(--red); font-family: "Arimo", sans-serif; font-style: italic; font-size: 20px; }
  .lead-copy .small { font-family: "Arimo", sans-serif; font-size: 17px; letter-spacing: 0; }
  .lead-copy .last { display: block; line-height: 20px; }

  .goodbye-heading {
    position: absolute; left: 0; top: 772px; width: 926px; text-align: center;
    font-family: "Fredoka", sans-serif; font-weight: 700; font-size: 60px;
    color: var(--royal); white-space: nowrap;
    -webkit-text-stroke: 5px var(--white); paint-order: stroke fill;
  }

  .contaminant-list {
    position: absolute; top: 856px; list-style: none;
    font-family: "Poppins", sans-serif; font-weight: 800; font-size: 25px;
    color: var(--ink); letter-spacing: -0.8px;
  }
  .contaminant-list.left { left: 125px; }
  .contaminant-list.right { left: 480px; }
  .contaminant-list li { display: flex; align-items: center; height: 34px; }
  .contaminant-list li span { text-decoration: line-through; text-decoration-thickness: 2px; }
  .cross-icon { width: 28px; height: 24px; margin-right: 10px; flex: none; }

  .contact-band {
    position: absolute; left: 0; top: 1043px; width: 926px; height: 92px;
    background: var(--royal);
  }
  .contact-label {
    position: absolute; left: 123px; top: 1047px;
    font-weight: 700; font-size: 29px; letter-spacing: 2.5px; color: var(--white);
  }
  .contact-number {
    position: absolute; left: 134px; top: 1076px;
    font-weight: 700; font-size: 54px; letter-spacing: 4px; color: var(--white);
  }
  .brand-sign {
    position: absolute; left: 690px; top: 1030px; width: 220px;
    font-family: "Fredoka", sans-serif; font-weight: 700; font-size: 44px;
    line-height: 1; color: var(--white); text-align: center;
  }
  .footer-strip {
    position: absolute; left: 0; top: 1135px; width: 926px; height: 30px;
    background: var(--band-cyan);
  }
  .footer-line {
    position: absolute; left: 30px; top: 1139px;
    font-weight: 700; font-size: 17px; color: var(--white); white-space: nowrap;
  }
</style>
</head>
<body>
<main class="flyer">
  <div class="sky"></div>
  <svg class="diagonal-band" width="926" height="260" viewBox="0 0 926 260">
    <polygon points="0,150 290,0 360,0 0,235" fill="#0d5cc0"/>
  </svg>
  <div class="cyan-band"></div>

  <div class="hostess-illustration" role="img" aria-label="Illustration of a waitress holding a tray with a bottle of water"></div>

  <div class="price-badge">
    <svg width="210" height="200" viewBox="0 0 210 200">
      <polygon fill="#d9262b" stroke="#ffffff" stroke-width="4"
        points="105,6 124,28 152,16 158,45 189,48 180,77 205,96 181,116 193,145 163,150 156,180 128,170 108,194 88,172 59,183 54,153 24,148 35,119 8,100 33,80 22,51 53,46 60,16 88,28"/>
    </svg>
    <div class="badge-text">
      <span class="only">only</span>
      <span class="amount"><small>€</small>2.99</span>
      <span class="week">week</span>
    </div>
  </div>

  <h1 class="headline-question">
    <span class="dark">Is it</span> <span class="light">time</span> <span class="dark">to</span> <span class="light">say</span>
  </h1>
  <p class="headline-brand">Tap Nest Flow</p>

  <h2 class="tagline-main">MAKING YOUR TAP WATER</h2>
  <p class="tagline-sub">SAFE &amp; DELICIOUS TO DRINK</p>

  <p class="lead-question">Sick and tired of having to buy expensive plastic bottled water?</p>
  <p class="lead-copy">
    Then, save on your weekly shopping with the new affordable <span class="brand-mention">TAP NEST FLOW</span>. All the delicious<br>
    clean and healthy water you can drink from your tap from only <span class="price">€ 2.99</span> <span class="small">a week. Including a</span>
    <span class="small last">FREE annual filter change.</span>
  </p>

  <h2 class="goodbye-heading">Say goodbye to</h2>

  <ul class="contaminant-list left">
    <li><svg class="cross-icon" viewBox="0 0 28 24"><path d="M3 3 L25 21 M25 3 L3 21" stroke="#0a55b8" stroke-width="6" stroke-linecap="round"/></svg><span>FOUL ODOURS</span></li>
    <li><svg class="cross-icon" viewBox="0 0 28 24"><path d="M3 3 L25 21 M25 3 L3 21" stroke="#0a55b8" stroke-width="6" stroke-linecap="round"/></svg><span>CRYPTOSPORIDIUM</span></li>
    <li><svg class="cross-icon" viewBox="0 0 28 24"><path d="M3 3 L25 21 M25 3 L3 21" stroke="#0a55b8" stroke-width="6" stroke-linecap="round"/></svg><span>CHLORINE</span></li>
    <li><svg class="cross-icon" viewBox="0 0 28 24"><path d="M3 3 L25 21 M25 3 L3 21" stroke="#0a55b8" stroke-width="6" stroke-linecap="round"/></svg><span>LEAD</span></li>
    <li><svg class="cross-icon" viewBox="0 0 28 24"><path d="M3 3 L25 21 M25 3 L3 21" stroke="#0a55b8" stroke-width="6" stroke-linecap="round"/></svg><span>PESTICIDES</span></li>
  </ul>
  <ul class="contaminant-list right">
    <li><svg class="cross-icon" viewBox="0 0 28 24"><path d="M3 3 L25 21 M25 3 L3 21" stroke="#0a55b8" stroke-width="6" stroke-linecap="round"/></svg><span>NASTY TASTES</span></li>
    <li><svg class="cross-icon" viewBox="0 0 28 24"><path d="M3 3 L25 21 M25 3 L3 21" stroke="#0a55b8" stroke-width="6" stroke-linecap="round"/></svg><span>INSECTICIDES</span></li>
    <li><svg class="cross-icon" viewBox="0 0 28 24"><path d="M3 3 L25 21 M25 3 L3 21" stroke="#0a55b8" stroke-width="6" stroke-linecap="round"/></svg><span>ARSENIC</span></li>
    <li><svg class="cross-icon" viewBox="0 0 28 24"><path d="M3 3 L25 21 M25 3 L3 21" stroke="#0a55b8" stroke-width="6" stroke-linecap="round"/></svg><span>TRIHALOMETHANES</span></li>
    <li><svg class="cross-icon" viewBox="0 0 28 24"><path d="M3 3 L25 21 M25 3 L3 21" stroke="#0a55b8" stroke-width="6" stroke-linecap="round"/></svg><span>SEDIMENT</span></li>
  </ul>

  <div class="contact-band"></div>
  <p class="contact-label">To Find Out More LoCall</p>
  <p class="contact-number">1890 555 017</p>
  <p class="brand-sign">Tap Nest<br>Flow</p>

  <div class="footer-strip"></div>
  <p class="footer-line">Clean, Healthy, Affordable &amp; Safe Drinking Water without the Bottle.</p>
</main>
</body>
</html>
```